Brightway Inc. Business Card Design

Brightway Inc. is in search of a great clean design for our business cards!

Looking to incorporate our full logo and watermark on side one (however, I am open to having the text and watermark separated within the design.)

On side two, I am looking to have contact information (Name, Position, Phone #, Email, Website (www.thebrightway.ca). Can have the logo and/or watermark as part of the design if applicable.

Please add tagline "Where Shine Counts" on either side 1 or 2. This tagline can be in a sans serif, serif or cursive font as long as it compliments overall design. Capitalization can be title or sentence case depending on how it fits within the design.

Get creative!! Looking for a clean, crisp, premium design! Looking for a glossy card finish with spot UV features when printed. Cards will also be printed with rounded corners. Standard dimensions (3.5 x 2).

Target Market(s)

B2B - primary clients are business owners or property management corporations. (residential jobs are few and far between)

Industry/Entity Type

Business

Contact Information for Business Card

- clean, crisp design
- double sided
- spot UV accents and glossy finish upon printing
- standard business card size (3.5 x 2) with rounded corners
- please see project description for requirements per side

Font styles to use
Sans Serif

Requirements
Must have
• - adequate bleeds with print ready files
• - cohesive design elements between side 1 & 2
• - spot UV elements (can be on both sides or just one, use your discretion)
• - colour pallet should match the logo file provided
• - incorporate tagline "where shine counts" (this tagline can be in a serif or sans serif font as long as it is complimentary to the overall design.
Nice to have
• - Premium elements with a clean design
Should not have
• - Please omit cartoon or whimsical like designs, think premium.
• - Colours should not stray from the pallet of the provided logo.

```html
<!DOCTYPE html>
<html lang="en">
<head>
<meta charset="utf-8">
<title>Brightway Inc. Business Cards</title>
<link href="https://fonts.googleapis.com/css2?family=Open+Sans:wght@400;600;700&family=Great+Vibes&display=swap" rel="stylesheet">
<style>
  :root {
    --backdrop: #e6e4df;
    --card-dark: #262626;
    --card-light: #ffffff;
    --teal: #3fc1b8;
    --teal-deep: #1f9e98;
    --navy: #1f2a55;
    --slate: #6f7aa6;
    --ink: #2b2b2b;
  }
  * { box-sizing: border-box; margin: 0; padding: 0; }
  html, body { width: 1200px; height: 800px; overflow: hidden; }
  body {
    background: var(--backdrop);
    font-family: "Open Sans", Arial, sans-serif;
    position: relative;
  }
  .card {
    position: absolute;
    left: 320px;
    width: 560px;
    height: 320px;
    border-radius: 18px;
    overflow: hidden;
    box-shadow: 0 8px 24px rgba(0,0,0,0.18);
  }
  /* Side one */
  .card-front { top: 50px; background: var(--card-dark); }
  .watermark-square {
    position: absolute;
    left: 215px; top: 70px;
    width: 150px; height: 150px;
    background: rgba(255,255,255,0.04);
  }
  .front-lockup {
    position: absolute;
    left: 0; right: 0; top: 105px;
    text-align: center;
  }
  .brand-name {
    font-weight: 700;
    letter-spacing: 1px;
    color: var(--teal);
    display: inline-flex;
    align-items: center;
    gap: 10px;
  }
  .brand-mark { display: inline-block; background: var(--teal); }
  .front-lockup .brand-name { font-size: 44px; }
  .front-lockup .brand-mark { width: 34px; height: 34px; }
  .tagline {
    font-family: "Great Vibes", cursive;
    color: var(--slate);
    font-size: 32px;
    margin-top: 2px;
    margin-left: 120px;
  }
  .front-web {
    position: absolute;
    left: 0; right: 0; top: 240px;
    text-align: center;
    color: var(--teal-deep);
    font-size: 14px;
  }
  /* Side two */
  .card-back { top: 430px; background: var(--card-light); }
  .back-logo { position: absolute; right: 36px; top: 34px; }
  .back-logo .brand-name { font-size: 30px; }
  .back-logo .brand-mark { width: 24px; height: 24px; }
  .back-web {
    position: absolute;
    right: 40px; top: 124px;
    color: var(--teal-deep);
    font-size: 14px;
    font-weight: 600;
  }
  .person {
    position: absolute;
    left: 36px; top: 160px;
    padding-left: 16px;
    border-left: 8px solid var(--teal);
  }
  .person-name { font-size: 28px; color: var(--navy); font-weight: 400; line-height: 1.1; }
  .person-title { font-size: 15px; color: var(--teal-deep); }
  .contact-list {
    position: absolute;
    left: 40px; bottom: 30px;
    list-style: none;
    font-size: 16px;
    color: var(--navy);
  }
  .contact-list li { display: flex; align-items: center; gap: 10px; margin-top: 8px; }
  .contact-list svg { width: 20px; height: 20px; fill: var(--teal); }
</style>
</head>
<body>
  <section class="card card-front">
    <div class="watermark-square"></div>
    <div class="front-lockup">
      <div class="brand-name"><span class="brand-mark"></span>BRIGHTWAY INC.</div>
      <p class="tagline">Where Shine Counts</p>
    </div>
    <p class="front-web">www.thebrightway.ca</p>
  </section>

  <section class="card card-back">
    <div class="back-logo">
      <div class="brand-name"><span class="brand-mark"></span>BRIGHTWAY INC.</div>
    </div>
    <p class="back-web">www.thebrightway.ca</p>
    <div class="person">
      <p class="person-name">Your Name</p>
      <p class="person-title">Job Title</p>
    </div>
    <ul class="contact-list">
      <li>
        <svg viewBox="0 0 24 24" aria-hidden="true"><path d="M3 9c0-3 4-5 9-5s9 2 9 5v2h-5V9H8v2H3z M6 12h12l2 8H4z"/></svg>
        000 000 0000
      </li>
      <li>
        <svg viewBox="0 0 24 24" aria-hidden="true"><path d="M2 5h20v14H2z M2 5l10 8 10-8" stroke="#fff" stroke-width="1.5"/></svg>
        youremail@xyz.com
      </li>
    </ul>
  </section>
</body>
</html>
```